Corvintal Real Estate Business Card

hello, we are a real estate company located in Los Angeles, california. we are a boutique, small company but we like a big corportate look. a simple, sleek, modern and progressive look. we would like the option of having a design that could include the real estate agents personal photo and also a design if the realtor desides not to have a photo. We also would like a hotizontal design.

Corvintal Properties
3817 N Halloway
West Hollywood, CA 90046
www.CorvintalRE.example

Glen Parrish
Broker
BRE # 04829175
(310) 555-0148
glen@corvintalre.example

Industry/Entity Type

Real Estate

```html
<!DOCTYPE html>
<html lang="en">
<head>
<meta charset="utf-8">
<title>Corvintal Real Estate Business Card</title>
<link rel="stylesheet" href="https://fonts.googleapis.com/css2?family=Lato:wght@400;700;900&display=swap">
<style>
  :root {
    --backdrop: #1d1d1f;
    --card: #111113;
    --brand-blue: #1f5ea8;
    --accent-blue: #2f8fd4;
    --ink: #f2f2f2;
  }
  * { box-sizing: border-box; margin: 0; padding: 0; }
  html, body {
    width: 1200px; height: 1000px; overflow: hidden;
    background: var(--backdrop);
    font-family: "Lato", sans-serif;
  }
  .canvas {
    position: relative; width: 1200px; height: 1000px;
  }
  .card {
    position: absolute; left: 220px;
    width: 760px; height: 430px;
    background: var(--card);
    border-radius: 14px;
    box-shadow: 0 18px 40px rgba(0,0,0,.55);
  }
  .card--back { top: 45px; }
  .card--front { top: 525px; }

  .wordmark {
    display: flex; align-items: center; gap: 22px;
    color: var(--brand-blue);
    font-weight: 700;
    letter-spacing: -1px;
  }
  .wordmark__square {
    width: 62px; height: 62px; background: var(--brand-blue);
  }
  .card--back .wordmark {
    position: absolute; left: 0; right: 0; top: 170px;
    justify-content: center; font-size: 92px; line-height: 1;
  }
  .card--front .wordmark {
    position: absolute; left: 60px; top: 70px;
    font-size: 76px; line-height: 1;
  }
  .card--front .wordmark__square { width: 52px; height: 52px; }
  .wordmark__sub { font-size: 76px; }

  .details {
    position: absolute; left: 0; right: 0; bottom: 48px;
    display: flex; justify-content: center; align-items: stretch;
  }
  .agent {
    text-align: right; padding-right: 24px;
    color: var(--ink); font-size: 19px; line-height: 1.45;
  }
  .agent__name {
    color: var(--brand-blue); font-weight: 900; font-size: 24px;
  }
  .divider { width: 2px; background: var(--ink); opacity: .85; }
  .contact {
    list-style: none; padding-left: 24px;
    color: var(--ink); font-size: 19px; line-height: 1.45;
  }
  .contact li { display: flex; gap: 12px; align-items: flex-start; }
  .contact svg { width: 20px; height: 20px; margin-top: 4px; flex: none; fill: var(--accent-blue); }
  .contact__indent { padding-left: 32px; }
</style>
</head>
<body>
<main class="canvas">
  <section class="card card--back" aria-label="Card back">
    <div class="wordmark">
      <span class="wordmark__square"></span>
      <span class="wordmark__name">corvintal</span>
    </div>
  </section>

  <section class="card card--front" aria-label="Card front">
    <div class="wordmark">
      <span class="wordmark__square"></span>
      <span class="wordmark__name">corvintal properties</span>
    </div>

    <div class="details">
      <div class="agent">
        <p class="agent__name">Glen Parrish</p>
        <p>Broker</p>
        <p>BRE # 04829175</p>
        <p>www.CorvintalRE.example</p>
      </div>
      <div class="divider"></div>
      <ul class="contact">
        <li>
          <svg viewBox="0 0 24 24" aria-hidden="true"><path d="M6.6 10.8a15.1 15.1 0 0 0 6.6 6.6l2.2-2.2c.3-.3.7-.4 1-.2 1.1.4 2.3.6 3.6.6.6 0 1 .4 1 1V20c0 .6-.4 1-1 1A17 17 0 0 1 3 4c0-.6.4-1 1-1h3.5c.6 0 1 .4 1 1 0 1.3.2 2.5.6 3.6.1.3 0 .7-.2 1z"/></svg>
          <span>(310) 555-0148</span>
        </li>
        <li>
          <svg viewBox="0 0 24 24" aria-hidden="true"><path d="M2 5h20v14H2zm2 2v.4l8 5.2 8-5.2V7zm0 2.8V17h16V9.8l-8 5.2z"/></svg>
          <span>glen@corvintalre.example</span>
        </li>
        <li>
          <svg viewBox="0 0 24 24" aria-hidden="true"><path d="M12 2a7 7 0 0 0-7 7c0 5.2 7 13 7 13s7-7.8 7-13a7 7 0 0 0-7-7zm0 9.5A2.5 2.5 0 1 1 12 6.5a2.5 2.5 0 0 1 0 5z"/></svg>
          <span>3817 N Halloway,</span>
        </li>
        <li class="contact__indent">West Hollywood, CA 90046</li>
      </ul>
    </div>
  </section>
</main>
</body>
</html>
```